Business Card Design Project

- makeup artist business card

- original and creative

- Elegant design

- Feel free to come out with cool designs but stick to being elegant and attractive

- Design relates to makeup

- includes name, occupation, contact numbers, email, website

- regular size business card

- round corner card

- double sided

- on 1 side it should just have the website name in the center " browsandblush.example "

Industry/Entity Type

Business

Requirements
Must have
• Marla Voss
Makeup Artist
USA: +1 (415)872-6410
Singapore: +65 83027715
marlavoss@browsandblush.example
www.browsandblush.example
Should not have
• nothing cartoon looking.
Pictures of makeup being grab from the internet.. Examples: eyes or lips.

```html
<!DOCTYPE html>
<html lang="en">
<head>
<meta charset="utf-8">
<title>Marla Voss – Makeup Artist</title>
<link rel="stylesheet" href="https://fonts.googleapis.com/css2?family=Arimo&family=Berkshire+Swash&family=Yanone+Kaffeesatz:wght@400&display=swap">
<style>
  :root {
    --card-dark: #2f2f2f;
    --card-glow: #6c6c6c;
    --blue-deep: #2f6fae;
    --blue-light: #4fc3f5;
    --ink-white: #ffffff;
    --ornament: rgba(255, 255, 255, 0.14);
  }
  html, body {
    margin: 0;
    padding: 0;
    width: 1200px;
    height: 726px;
    overflow: hidden;
    background: #ffffff;
  }
  .card {
    position: relative;
    width: 1200px;
    height: 726px;
    overflow: hidden;
    background: radial-gradient(ellipse 720px 520px at 760px 0px, var(--card-glow), var(--card-dark) 80%);
    color: var(--ink-white);
  }
  .pattern-panel {
    position: absolute;
    left: 0; top: 0;
    width: 430px; height: 726px;
    background: linear-gradient(135deg, var(--blue-light) 0%, #3b93d6 55%, var(--blue-deep) 100%);
  }
  .crown-ornament {
    position: absolute;
    left: 675px; top: 17px;
    width: 280px; height: 60px;
    background: radial-gradient(ellipse at center, rgba(255,255,255,0.35), rgba(255,255,255,0) 70%);
  }
  .swirl-ornament {
    position: absolute;
    left: 737px; top: 67px;
    width: 463px; height: 659px;
    background: radial-gradient(ellipse at 60% 50%, var(--ornament), rgba(255,255,255,0) 70%);
  }
  .brand-name {
    position: absolute;
    left: 0; top: 330px;
    width: 430px;
    text-align: center;
    font-family: "Arimo", Arial, sans-serif;
    font-size: 58px;
    line-height: 1;
    color: var(--ink-white);
  }
  .title-block {
    position: absolute;
    left: 560px; top: 64px;
    width: 520px;
    text-align: center;
  }
  .title-name {
    margin: 0;
    font-family: "Berkshire Swash", Georgia, serif;
    font-weight: 400;
    font-size: 76px;
    line-height: 1;
    letter-spacing: 2px;
  }
  .title-role {
    margin: 4px 0 0;
    font-family: "Yanone Kaffeesatz", "Arial Narrow", sans-serif;
    font-size: 44px;
    line-height: 1;
    letter-spacing: 1px;
  }
  .contact {
    position: absolute;
    right: 33px; top: 428px;
    margin: 0; padding: 0;
    list-style: none;
    text-align: right;
    font-family: "Arimo", Arial, sans-serif;
    font-size: 33px;
  }
  .contact li {
    height: 58px;
    line-height: 40px;
  }
</style>
</head>
<body>
  <div class="card">
    <div class="pattern-panel" role="img" aria-label="Repeating monogram pattern in shades of blue"></div>
    <div class="swirl-ornament" role="img" aria-label="Faint decorative swirl flourishes"></div>
    <div class="crown-ornament" role="img" aria-label="Small crown and scroll ornament above the name"></div>

    <div class="brand-name">Marla Voss</div>

    <header class="title-block">
      <h1 class="title-name">Marla Voss</h1>
      <p class="title-role">Makeup Artist</p>
    </header>

    <ul class="contact">
      <li>Makeup Artist</li>
      <li>USA: +1 (415)872-6410</li>
      <li>Singapore: +65 83027715</li>
      <li>marlavoss@browsandblush.example</li>
      <li>www.browsandblush.example</li>
    </ul>
  </div>
</body>
</html>
```